Coaching Workbook (for life & health coaching industry)

I created a coaching workbook using Canva. I would like it recreated more professionally in PowerPoint with better images and creative design using my 3 branding colors (teal primary, salmon secondary, and turquoise splash here and there).

Please use the attached image of lady sitting on dock at the lake on the first slide for the cover along with my logo and my titles (similar to my Canva version on my website).

My version of the workbook is attached. Thank you for turning my drab into fab:-) Merle Quistad, Life & Health Coach, Grief Recovery Specialist
Updates

To ensure clarity, I am looking for a PowerPoint (prefer vertical format) for a coaching manual FROM the material in the version that I created in Canva, which is currently on my website as a download at the bottom of my coaching page: https://brightmeadowguide.example/coaching-2 I will upload the pdf file as well as the example that I'm trying to recreate in PowerPoint, but more professionally and creatively. Thank You! Merle Quistad

Target Market(s)

My target audience is primarily female, with a few males each year, ages range from mid-twenties to sixties. Everyone will experience the pain of loss and grief. Women are more prone to reach out for help sooner.

Industry/Entity Type

Life Coaching

Font styles to use
Serif

Requirements
Must have
• Want it to feel personal, not corporate if that makes sense.
• Must use my 3 branding colors: HEX # 2994ae, 10dfd3, fa8070.
• Please use Playfair Display font for consistency with my website.
• The text for the workbook is included in the Word document attached below.
Should not have
• I'm not looking for the material on my website to be the focus of this workbook. I want the Canva version that I created to be converted more professionally and creatively in PowerPoint, so I can manage moving forward.

```html
<!DOCTYPE html>
<html lang="en">
<head>
<meta charset="UTF-8">
<title>Workbook Slide 13 – Reflection</title>
<link rel="stylesheet" href="https://fonts.googleapis.com/css2?family=Playfair+Display:wght@700;800&family=Poppins:wght@300;400;600;700&display=swap">
<style>
  :root {
    --stage: #3a3b3d;
    --paper: #ffffff;
    --salmon: #fa8070;
    --teal: #2994ae;
    --turquoise: #10dfd3;
    --link: #1ea0cf;
    --ink: #3a3a3a;
    --ink-strong: #2b2b2b;
  }
  * { box-sizing: border-box; margin: 0; padding: 0; }
  html, body {
    width: 1200px; height: 1200px; overflow: hidden;
    background: var(--stage);
  }
  .canvas {
    position: relative; width: 1200px; height: 1200px;
    background: var(--stage);
  }
  .page {
    position: absolute; left: 129px; top: 110px;
    width: 641px; height: 844px;
    background: var(--paper);
  }
  .page-header {
    height: 60px; background: var(--salmon);
    display: flex; align-items: center; justify-content: center;
  }
  .page-title {
    font-family: "Playfair Display", Georgia, serif;
    font-weight: 800; font-size: 45px; color: var(--paper);
    line-height: 1; margin-top: 2px;
  }
  .page-body {
    padding: 25px 42px 0 27px;
    font-family: "Poppins", Arial, sans-serif;
    font-weight: 300; font-size: 11.2px; line-height: 15.5px;
    color: var(--ink);
  }
  .page-body p { margin-bottom: 27px; }
  .page-body a { color: var(--link); text-decoration: underline; }
  .signoff {
    position: absolute; left: 27px; top: 668px;
    font-family: "Poppins", Arial, sans-serif;
  }
  .signoff-greeting {
    font-weight: 600; font-size: 10.5px; color: var(--ink-strong);
  }
  .signoff-name {
    margin-top: 6px; font-weight: 700; font-size: 31px;
    letter-spacing: 0.3px; line-height: 1; color: var(--salmon);
  }
  .signoff-role {
    margin-top: 10px; font-weight: 600; font-size: 15.5px;
    letter-spacing: -0.4px; color: var(--teal);
  }
  .brand-mark {
    position: absolute; left: 29px; top: 780px;
    display: flex; align-items: center; gap: 8px;
    font-family: "Poppins", Arial, sans-serif;
    font-weight: 400; font-size: 13px; letter-spacing: 2px;
    color: var(--teal); text-transform: uppercase;
  }
  .brand-dot {
    width: 10px; height: 10px; border-radius: 50%;
    background: var(--teal);
  }
  .slide-label {
    position: absolute; left: 1050px; top: 616px;
    transform: translate(-50%, -50%) rotate(-90deg);
    font-family: "Poppins", Arial, sans-serif;
    font-weight: 300; font-size: 140px; line-height: 1;
    color: var(--salmon); white-space: nowrap;
  }
</style>
</head>
<body>
<main class="canvas">
  <article class="page">
    <header class="page-header">
      <h1 class="page-title">Reflection</h1>
    </header>
    <section class="page-body">
      <p>I’ve had three knee surgeries because I love tennis too much to ever stop playing (and I definitely wasn’t going to let a little thing like a damaged knee stop me!). After each surgery, I followed the recommended physical therapy to maximize my healing. The therapy was painful. What if I had let the fear of the pain of physical therapy win? What if I had tried to push thoughts to the back of my mind, pretending I wasn’t injured at all?</p>
      <p>I would have avoided the short-term intense pain and hard work, alright. But I also would have been saddled with a lifetime of low-level knee pain, restricted motion, and no more tennis. If I hadn’t done physical therapy, my quality of life would have diminished, forever.</p>
      <p>Just as it is with physical injuries, so it is with emotional injuries. If you experience a loss, trauma, or any kind of emotional stress (as we all have!) and you ignore or avoid your feelings, the rest of your life will be subconsciously affected by that pain.</p>
      <p>However, unlike with physical injuries, where the pain is validated by the world, emotional injuries are easily unnoticed or dismissed by you and others. That makes it harder to address in the moment.</p>
      <p>Fortunately, rehab for your heart can begin at any time. That’s where the Heart Renewal Method comes in, with me as your coach to guide you through the process of dealing with unresolved pains and losses.</p>
      <p>After you complete the Heart Renewal Method Program, my life and health coaching packages continue building on your incredible progress to improve your life in other areas, like mindfulness, healthy habits, relationships, and goal setting.</p>
      <p>Today, the scars from my knee surgeries are still visible, reminding me of my limitations and my need for continued self-reflection and healing. Right now, you may have emotional scars invisible to the outside world. But that doesn’t mean they’re not there, limiting your full potential for joy.</p>
      <p><a href="https://brightmeadowguide.example/coaching-2">Schedule</a> a complimentary discovery coaching session with me to discuss your next best steps in living your best life.</p>
    </section>
    <footer class="signoff">
      <p class="signoff-greeting">In Wellness,</p>
      <p class="signoff-name">MERLE QUISTAD</p>
      <p class="signoff-role">LIFE &amp; HEALTH COACH, GRIEF RECOVERY SPECIALIST</p>
    </footer>
    <div class="brand-mark">
      <span class="brand-dot"></span>
      <span>Bright Meadow Coaching</span>
    </div>
  </article>
  <div class="slide-label">slide 13</div>
</main>
</body>
</html>
```